Business Card Design Project

Bold, modern, clean business card design needed. Prefer double sided with art logo on the back. Front of card with company name logo, no art.

Target Market(s)

Our consulting company supports local, state and federal law enforcement officers. Therefore the design should be clean and direct with no flash or arrogance to it.

Industry/Entity Type

Business

```html
<!DOCTYPE html>
<html lang="en">
<head>
<meta charset="utf-8">
<title>Talvoren Consulting – Business Card</title>
<link href="https://fonts.googleapis.com/css2?family=Orbitron:wght@400;600&display=swap" rel="stylesheet">
<style>
  :root {
    --canvas: #e9eaea;
    --paper: #ffffff;
    --ink: #1b1b1b;
    --green: #8cc63f;
    --green-dark: #6fa52b;
    --night: #1a1c1b;
    --night-edge: #070807;
    --silver: #c9cccc;
    --muted: #3a3a3a;
  }
  * { box-sizing: border-box; margin: 0; padding: 0; }
  html, body {
    width: 1200px; height: 873px; overflow: hidden;
    background: var(--canvas);
    font-family: "Orbitron", sans-serif;
  }
  .stage {
    width: 1200px; height: 873px;
    display: flex; align-items: center; justify-content: center; gap: 40px;
  }
  .card {
    position: relative; width: 520px; height: 298px; overflow: hidden;
    box-shadow: 0 6px 18px rgba(0,0,0,.18);
  }

  /* Front */
  .card--front { background: var(--paper); color: var(--ink); }
  .wordmark { position: absolute; display: flex; align-items: center; gap: 12px; }
  .card--front .wordmark { left: 34px; top: 34px; color: var(--ink); }
  .wordmark__dot { width: 34px; height: 34px; border-radius: 50%; background: var(--green); flex: none; }
  .wordmark__name { font-weight: 600; line-height: 1; }
  .wordmark__main { display: block; font-size: 28px; letter-spacing: 2px; }
  .wordmark__sub { display: block; font-size: 10px; letter-spacing: 6.2px; margin-top: 5px; }

  .holder {
    position: absolute; right: 34px; top: 112px;
    font-size: 16px; font-weight: 400; letter-spacing: 1.5px;
  }
  .contact-list {
    position: absolute; right: 34px; top: 146px; list-style: none;
    display: flex; flex-direction: column; gap: 8px; align-items: flex-end;
  }
  .contact-list li {
    display: flex; align-items: center; gap: 10px;
    font-size: 9.5px; letter-spacing: 1px; color: var(--muted);
  }
  .icon {
    width: 16px; height: 16px; border-radius: 50%; background: var(--green);
    display: flex; align-items: center; justify-content: center; flex: none;
  }
  .icon svg { width: 10px; height: 10px; fill: #fff; }
  .website {
    position: absolute; left: 34px; bottom: 28px;
    display: flex; align-items: center; gap: 10px;
    font-size: 10px; letter-spacing: 1.2px; color: var(--muted);
  }

  /* Back */
  .card--back {
    background: radial-gradient(ellipse at 62% 45%, var(--night) 0%, #121312 55%, var(--night-edge) 100%);
  }
  .card--back .band {
    position: absolute; left: 0; top: 0; bottom: 0; width: 70px;
    background: linear-gradient(90deg, var(--green-dark), var(--green) 60%, #9ed24f);
  }
  .card--back .band-edge {
    position: absolute; left: 70px; top: 0; bottom: 0; width: 8px;
    background: linear-gradient(90deg, #e6e8e8, var(--silver));
  }
  .card--back .wordmark {
    left: 78px; right: 0; top: 0; bottom: 0; justify-content: center; color: var(--silver);
  }
  .card--back .wordmark__dot { width: 46px; height: 46px; }
  .card--back .wordmark__main { font-size: 36px; letter-spacing: 3px; }
  .card--back .wordmark__sub { font-size: 12.5px; letter-spacing: 8.6px; margin-top: 7px; }
</style>
</head>
<body>
<main class="stage">
  <section class="card card--front" aria-label="Business card front">
    <div class="wordmark">
      <span class="wordmark__name">
        <span class="wordmark__main">TALVOREN</span>
        <span class="wordmark__sub">CONSULTING</span>
      </span>
      <span class="wordmark__dot"></span>
    </div>

    <p class="holder">Daniel Reeve</p>

    <ul class="contact-list">
      <li>555 204 318
        <span class="icon"><svg viewBox="0 0 10 10"><path d="M2 1l2 2-1 1.2c.6 1.2 1.6 2.2 2.8 2.8L7 6l2 2-1.2 1.5C4.5 9.2.8 5.5.5 2.2z"/></svg></span>
      </li>
      <li>YOUR ADDRESS NO.65
        <span class="icon"><svg viewBox="0 0 10 10"><path d="M5 .5a3.2 3.2 0 0 0-3.2 3.2C1.8 6.3 5 9.5 5 9.5s3.2-3.2 3.2-5.8A3.2 3.2 0 0 0 5 .5zm0 4.5a1.3 1.3 0 1 1 0-2.6 1.3 1.3 0 0 1 0 2.6z"/></svg></span>
      </li>
      <li>FEED/NAME <span class="icon"></span></li>
      <li>PROFILE/NAME <span class="icon"></span></li>
      <li>YOUR@EMAIL.COM
        <span class="icon"><svg viewBox="0 0 10 10"><path d="M1 2.5h8v5H1z M1 2.5l4 3 4-3" fill="none" stroke="#fff" stroke-width="1"/></svg></span>
      </li>
    </ul>

    <p class="website">
      <span class="icon"><svg viewBox="0 0 10 10"><path d="M1 4.5L9 1 5.5 9 4.6 5.4z"/></svg></span>
      WWW.YOURWEBSITE.COM
    </p>
  </section>

  <section class="card card--back" aria-label="Business card back">
    <div class="band"></div>
    <div class="band-edge"></div>
    <div class="wordmark">
      <span class="wordmark__name">
        <span class="wordmark__main">TALVOREN</span>
        <span class="wordmark__sub">CONSULTING</span>
      </span>
      <span class="wordmark__dot"></span>
    </div>
  </section>
</main>
</body>
</html>
```